Letterhead for 3 attorney Workers' Comp law firm

We are a 3 attorney law office. We specialize in Workers' Compensation. Our office represents workers who are injured on the job, and the estates of workers who are killed one the job.
When we started our office, we created our own letterhead & have been using it for years. We've just recently hired the 3rd attorney, and were going to just add his name to the letterhead, but have decided we wanted to get a professionally designed letterhead and business cards at this point.
We want something that looks clean and professional. It must look good in black and white because we often make multiple copies of our documents. We're hoping for a design that resonates confidence, reliability and experience.
The design must include the firm name: Dorrance & Pike, PLLC. We would like the PLLC to be small compared to the Dorrance & Pike graphic. We also want to incorporate the attorney names: Ulric Dorrance, Janet Pike, and Lyle Hagberg. Our current letterhead has our contact info in the footer at the bottom of the page. We like that design, but are open to the idea of having it at the top. We'll leave that at the discretion of the designer. Our contact info is as follows: 472 S. Larchmont Avenue, Suite 315 Bellingham, WA 98117 Phone: 360-514-2967, Fax: 360-521-6079, and our website: www.dorrancepike-law.example
Target Market(s)
Clients, courts, other legal offices, doctors offices. These are the people who see our letterhead most frequently. It's not so much for marketing purposes, mainly so that we have a professional image when sending out documents.
Industry/Entity Type
Law Firm
Contact Information for Business Card
On the back of the business card: it can be designed, or be a template for filling in appointment reminder information (i.e. date, time, etc)
Colors
Designer to choose colors to be used in the design.
Requirements
Must have
- Must have our firm name at the top.
- Must include the attorney names.
- Must have all of our contact information (can be at top or bottom - whatever looks best with the design)
Nice to have
- A strong, confident design
Should not have
- We don't want the design to be playful, cartoony or busy.

```html
<!DOCTYPE html>
<html lang="en">
<head>
<meta charset="utf-8">
<title>Dorrance &amp; Pike, PLLC — Letterhead</title>
<link rel="stylesheet" href="https://fonts.googleapis.com/css2?family=Arimo:ital,wght@0,400;0,700;1,400&display=swap">
<style>
  :root {
    --backdrop: #e4e4e4;
    --paper: #ffffff;
    --ink: #1e1e1e;
    --body-ink: #3a3a3a;
    --muted: #6e6e6e;
    --rule-strong: #2a2a2a;
    --rule-soft: #b5b5b5;
    --accent-grey: #8a8a8a;
  }
  * { box-sizing: border-box; margin: 0; padding: 0; }
  html, body {
    width: 1200px; height: 931px; overflow: hidden;
    background: var(--backdrop);
    font-family: "Arimo", Arial, sans-serif;
    color: var(--ink);
  }
  .letterhead {
    position: absolute; left: 285px; top: 24px;
    width: 630px; height: 882px;
    background: var(--paper);
  }
  .letterhead > * { position: absolute; }

  /* Firm name */
  .firm-name {
    right: 56px; top: 56px; text-align: right;
    font-weight: 700; color: var(--ink); line-height: 1;
  }
  .firm-name .firm-main { font-size: 33px; letter-spacing: -0.5px; }
  .firm-name .firm-suffix { font-size: 13px; letter-spacing: 1px; }
  .tagline {
    right: 56px; top: 133px;
    font-size: 9.5px; font-style: italic; color: var(--ink);
  }

  /* Rules */
  .rule { height: 0; }
  .rule--side { left: 61px; width: 95px; border-top: 1.5px solid var(--rule-strong); }
  .rule--main { left: 177px; width: 397px; border-top: 1px solid var(--rule-soft); }
  .rule--top { top: 160px; }
  .rule--bottom { top: 807px; }

  /* Attorney list */
  .attorneys { left: 61px; top: 209px; }
  .attorneys h2 { font-size: 13px; font-weight: 700; margin-bottom: 11px; }
  .attorneys ul { list-style: none; }
  .attorneys li {
    display: flex; align-items: center; gap: 9px;
    font-size: 10.5px; font-weight: 700; height: 25.5px;
  }
  .attorneys .marker {
    width: 13px; height: 13px; border-radius: 50%;
    background: var(--accent-grey); flex: none;
  }

  /* Letter content */
  .recipient {
    left: 177px; top: 211px;
    font-size: 9.5px; line-height: 12.3px; color: var(--body-ink);
  }
  .letter-body {
    left: 177px; top: 286px; width: 397px;
    font-size: 9.4px; line-height: 11.3px; color: var(--body-ink);
    text-align: justify;
  }
  .letter-body p { margin-bottom: 11.3px; }
  .closing {
    left: 177px; top: 664px;
    font-size: 9.5px; color: var(--body-ink);
  }
  .signature {
    left: 177px; top: 718px;
    font-size: 9.5px; line-height: 12.5px; color: var(--body-ink);
  }

  /* Contact footer */
  .contact { font-size: 9.5px; color: var(--body-ink); line-height: 1; }
  .contact svg { position: absolute; left: 0; top: -1px; width: 10px; height: 10px; fill: var(--ink); }
  .contact-address { left: 179px; top: 815px; padding-left: 12px; line-height: 17px; }
  .contact-address svg { top: 3px; }
  .contact-phone { left: 353px; top: 814px; padding-left: 13px; font-size: 12.5px; font-weight: 700; color: var(--ink); }
  .contact-phone svg { top: 1px; }
  .contact-fax { left: 457px; top: 815px; padding-left: 13px; }
  .contact-web { left: 353px; top: 832px; padding-left: 13px; }
  .contact-web strong { font-weight: 700; color: var(--ink); }
</style>
</head>
<body>
<main class="letterhead">

  <div class="firm-name"><span class="firm-main">Dorrance &amp; Pike</span><span class="firm-suffix">, PLLC</span></div>
  <p class="tagline">specialize in Workers' Compensation</p>

  <div class="rule rule--side rule--top"></div>
  <div class="rule rule--main rule--top"></div>

  <section class="attorneys">
    <h2>Attorney</h2>
    <ul>
      <li><span class="marker"></span>Ulric Dorrance</li>
      <li><span class="marker"></span>Janet Pike</li>
      <li><span class="marker"></span>Lyle Hagberg</li>
    </ul>
  </section>

  <address class="recipient" style="font-style:normal">
    Mr. Howard Lindqvist<br>
    Managing Director<br>
    Northgate Holdings<br>
    240 W Alder Street<br>
    USA
  </address>

  <article class="letter-body">
    <p>Lorem ipsum dolor sit amet, consectetuer adipiscing elit. Nam cursus. Morbi ut mi. Nullam enim leo, egestas id, condimentum at, laoreet mattis, massa. Sed eleifend nonummy diam. Praesent mauris ante, elementum et, bibendum at, posuere sit amet, nibh. Duis tincidunt lectus quis dui viverra vestibulum.</p>
    <p>Suspendisse vulputate aliquam dui. Nulla elementum dui ut augue. Aliquam vehicula mi at mauris. Maecenas placerat, nisl at consequat rhoncus, sem nunc gravida justo, quis eleifend arcu velit quis lacus. Morbi magna magna, tincidunt a, mattis non, imperdiet vitae, tellus. Sed odio est, auctor ac, sollicitudin in, consequat vitae, orci. Fusce id felis. Vivamus sollicitudin.</p>
    <p>Metus eget eros. Pellentesque habitant morbi tristique senectus et netus et malesuada fames ac turpis egestas. In posuere felis nec tortor. Pellentesque faucibus. Ut accumsan ultricies elit. Maecenas at justo id velit placerat molestie. Donec dictum lectus non odio. Cras a ante vitae enim iaculis aliquam.</p>
    <p>Mauris nunc quam, venenatis nec, euismod sit amet, egestas placerat, est. Pellentesque habitant morbi tristique senectus et netus et malesuada fames ac turpis egestas. Cras id elit. Integer quis urna. Ut ante enim, dapibus malesuada, fringilla eu, condimentum quis, tellus. Aenean porttitor eros vel dolor. Donec convallis pede venenatis nibh. Duis quam. Nam eget.</p>
    <p>Mauris nunc quam, venenatis nec, euismod sit amet, egestas placerat, est. Pellentesque habitant morbi tristique senectus et netus et malesuada fames ac turpis egestas. Cras id elit. Integer quis urna. Ut ante enim, dapibus malesuada, fringilla eu, condimentum quis, tellus. Aenean porttitor eros vel dolor. Donec convallis pede venenatis nibh. Duis quam. Nam eget.</p>
    <p>Mauris nunc quam, venenatis nec, euismod sit amet, egestas placerat, est. Pellentesque habitant morbi tristique senectus et netus et malesuada fames ac turpis egestas. Cras id elit. Integer quis urna. Ut ante enim, dapibus malesuada, fringilla eu, condimentum quis, tellus. Aenean porttitor eros vel dolor. Donec convallis pede venenatis nibh. Duis quam. Nam eget.</p>
  </article>

  <p class="closing">Thank you for being one of our valued customers.</p>
  <p class="signature">Name Here<br>CEO</p>

  <div class="rule rule--side rule--bottom"></div>
  <div class="rule rule--main rule--bottom"></div>

  <div class="contact contact-address">
    <svg viewBox="0 0 10 10" aria-hidden="true"><path d="M5 0.5a3.3 3.3 0 0 0-3.3 3.3C1.7 6.3 5 9.5 5 9.5s3.3-3.2 3.3-5.7A3.3 3.3 0 0 0 5 0.5zm0 4.6a1.3 1.3 0 1 1 0-2.6 1.3 1.3 0 0 1 0 2.6z"/></svg>
    472 S. Larchmont Avenue,<br>Suite 315 Bellingham, WA 98117
  </div>
  <div class="contact contact-phone">
    <svg viewBox="0 0 10 10" aria-hidden="true"><path d="M2.2 0.6l1.6 1.9-0.9 1.2c0.6 1.3 1.6 2.3 2.9 2.9l1.2-0.9 1.9 1.6-0.8 1.5C4.6 9 1 5.4 0.7 1.4z"/></svg>
    360-514-2967
  </div>
  <div class="contact contact-fax">
    <svg viewBox="0 0 10 10" aria-hidden="true"><path d="M2.5 0.8h5v2.4h-5zM1 3.8h8v3.6H7.5V9h-5V7.4H1zm2.5 2.4V8h3V6.2z"/></svg>
    360-521-6079
  </div>
  <div class="contact contact-web">
    <svg viewBox="0 0 10 10" aria-hidden="true"><path d="M5 0.5a4.5 4.5 0 1 0 0 9 4.5 4.5 0 0 0 0-9zm0 1c0.6 0.6 1 1.7 1.1 3H3.9C4 3.2 4.4 2.1 5 1.5zM2.9 4.5H1.6a3.5 3.5 0 0 1 2.1-2.7c-0.5 0.7-0.8 1.7-0.8 2.7zm0 1c0 1 0.3 2 0.8 2.7a3.5 3.5 0 0 1-2.1-2.7zm1 0h2.2C6 6.8 5.6 7.9 5 8.5 4.4 7.9 4 6.8 3.9 5.5zm3.2 0h1.3a3.5 3.5 0 0 1-2.1 2.7c0.5-0.7 0.8-1.7 0.8-2.7zm0-1c0-1-0.3-2-0.8-2.7a3.5 3.5 0 0 1 2.1 2.7z"/></svg>
    www.<strong>dorrancepike-law</strong>.example
  </div>

</main>
</body>
</html>
```